Website for Trayvora.net - a web site to market and sell our online school lunch ordering system.

We need a web site to market and engage our online school lunch ordering software. Caterers all over United States are looking for a software that helps them grow by replacing paper based systems with online ordering systems that parents can use to place lunch orders for their kids. Our mobile app compliments our web app by giving parents the freedom to order when they are not in front of their computers or at home. We would like to see designs that can engage our prospects by telling a compelling story about our product with features, metrics, product tours and screenshots.

```html
<!DOCTYPE html>
<html lang="en">
<head>
<meta charset="utf-8">
<title>Trayvora Site</title>
<link rel="stylesheet" href="https://fonts.googleapis.com/css2?family=Montserrat:wght@400;600;700;800&display=swap">
<style>
:root{
  --blue:#0b8fd0;
  --orange:#f4682f;
  --mustard:#e08a2e;
  --navy:#141a52;
  --white:#ffffff;
  --ink:#111111;
  --green-light:#7cc576;
  --green-dark:#0f6b2e;
  --dot-pink:#e0167a;
  --dot-orange:#f26a1b;
}
*{margin:0;padding:0;box-sizing:border-box}
html,body{width:1200px;height:1200px;overflow:hidden;background:var(--white)}
body{position:relative;font-family:"Montserrat",sans-serif;color:var(--white)}
.abs{position:absolute}
.btn{position:absolute;display:flex;align-items:center;justify-content:center;font-weight:700;border-radius:4px;color:var(--white)}
.btn-navy{background:var(--navy);font-size:15px}
.btn-orange{background:var(--orange)}

/* hero */
.hero-photo{left:0;top:0;width:772px;height:218px;background:radial-gradient(ellipse at 55% 40%,#c9503c 0%,#d9a98a 30%,#ece4dc 60%,#ddd6cf 100%)}
.site-title{left:148px;top:-5px;font-size:30px;font-weight:800;letter-spacing:1px;text-shadow:0 1px 3px rgba(0,0,0,.4)}
.hero-title{left:0;width:876px;top:60px;text-align:center;font-size:37px;font-weight:800;letter-spacing:2px;text-shadow:0 1px 3px rgba(0,0,0,.4)}
.hero-sub{left:0;width:812px;top:94px;text-align:center;font-size:23.5px;font-weight:400;text-shadow:0 1px 3px rgba(0,0,0,.4)}
.side-panel{left:772px;top:0;width:428px;height:218px;background:var(--blue)}
.user-badge{left:896px;top:4px;width:62px;height:26px;border-radius:50%;background:var(--orange)}
.side-btn{left:833px;width:149px;height:44px;font-size:10.5px;letter-spacing:.5px}

/* menu band */
.menu-photo{left:0;top:218px;width:1200px;height:193px;background:linear-gradient(100deg,#6a5c52 0%,#8e7764 35%,#a58a63 60%,#7d6650 100%)}
.menu-copy{left:556px;top:230px;width:484px;font-size:11.8px;line-height:9px;font-weight:400}
.menu-btn{left:360px;top:362px;width:164px;height:33px;font-size:15px}

/* card sections */
.band{left:0;width:1200px;background:var(--mustard)}
.band-title{left:0;text-align:center;font-size:15px;font-weight:700;letter-spacing:.5px}
.card-icon{width:90px;height:38px}
.card-text{width:220px;font-size:10.4px;line-height:16.4px;letter-spacing:.4px;color:#fbe6cc;white-space:nowrap}
.card-btn{width:124px;height:26px}

/* sales */
.sales-title{left:154px;top:613px;font-size:15px;font-weight:800;color:var(--ink);letter-spacing:.6px}
.sales-copy{left:153px;top:630px;width:360px;font-size:11.4px;line-height:9px;font-weight:700;color:var(--ink)}
.chart{left:534px;top:604px;width:509px;height:215px}

/* footer */
.footer{left:0;top:1028px;width:1200px;height:172px;background:var(--blue)}
.footer-nav{left:0;width:1324px;top:1030px;text-align:center;font-size:13px;font-weight:700;letter-spacing:.3px}
.contact{left:154px;top:1053px;font-size:12px;line-height:16.4px;font-weight:700;font-style:normal}
.footer-copy{left:342px;top:1056px;width:712px;font-size:8.6px;line-height:13.8px}
.footer-link{top:1178px;font-size:17.5px;font-weight:400;letter-spacing:.5px}
.social{top:1158px;width:20px;height:20px;border-radius:50%;border:2px solid var(--white)}
.connect{left:534px;top:1180px;font-size:17px;font-weight:700;letter-spacing:.5px}
</style>
</head>
<body>

<!-- hero -->
<div class="abs hero-photo" role="img" aria-label="Close-up photo of a pepperoni pizza slice on a plate"></div>
<div class="abs site-title">Trayvora Site</div>
<div class="abs hero-title">Fresh Ingredients</div>
<div class="abs hero-sub">School Meals You'll Love!</div>
<div class="btn btn-navy" style="left:336px;top:158px;width:164px;height:33px">Order Now</div>

<div class="abs side-panel"></div>
<div class="abs user-badge"></div>
<svg class="abs" style="left:912px;top:6px" width="30" height="22" viewBox="0 0 30 22" fill="none" stroke="#fff" stroke-width="1.6">
  <circle cx="15" cy="8" r="5"/><path d="M4 21c1-5 6-7 11-7s10 2 11 7"/>
</svg>
<div class="btn btn-orange side-btn" style="top:40px">Ingredients</div>
<div class="btn btn-orange side-btn" style="top:90px">Our Missions</div>
<div class="btn btn-orange side-btn" style="top:139px">Contact Us</div>

<!-- menu band -->
<div class="abs menu-photo" role="img" aria-label="Photo of a table with potato wedges, dipping sauces and tortilla chips"></div>
<p class="abs menu-copy">Lorem ipsum dolor sit amet, consectetur adipisicing elit, sed do eiusmod tempor incididunt ut labore et dolore magna aliqua. Ut enim ad minim veniam, quis nostrud exercitation ullamco laboris nisi ut aliquip ex ea commodo consequat. Duis aute irure dolor in reprehenderit in voluptate velit esse cillum dolore eu fugiat nulla pariatur. Excepteur sint occaecat cupidatat non proident, sunt in culpa qui officia deserunt mollit anim id est laborum. Sed ut perspiciatis unde omnis iste natus error sit voluptatem accusantium doloremque laudantium, totam rem aperiam, eaque ipsa quae ab illo inventore veritatis et quasi architecto beatae vitae dicta sunt explicabo. Nemo enim ipsam voluptatem quia voluptas sit aspernatur aut odit aut fugit, sed quia consequuntur magni dolores eos qui ratione voluptatem sequi nesciunt. Neque porro quisquam est, qui dolorem ipsum quia dolor sit amet, consectetur, adipisci velit, sed quia non numquam eius modi tempora incidunt ut labore et dolore</p>
<div class="btn btn-orange menu-btn">View Full Menu</div>

<!-- mission -->
<div class="abs band" style="top:411px;height:195px"></div>
<div class="abs band-title" style="top:416px;width:1210px">OUR MISSION</div>

<svg class="abs card-icon" style="left:197px;top:436px" viewBox="0 0 90 46" fill="none" stroke="#fff" stroke-width="2">
  <path d="M12 32a33 26 0 0 1 66 0"/><path d="M6 34h78"/><circle cx="45" cy="5" r="3"/><path d="M22 40h46"/>
</svg>
<svg class="abs card-icon" style="left:445px;top:436px" viewBox="0 0 90 46" fill="none" stroke="#fff" stroke-width="2">
  <path d="M10 4l56 38"/><path d="M10 4l6 -3M14 7l6-3M18 10l6-3"/><path d="M82 6c-6-4-16 2-18 10L22 42"/>
</svg>
<svg class="abs card-icon" style="left:665px;top:436px" viewBox="0 0 90 46" fill="none" stroke="#fff" stroke-width="2">
  <path d="M30 26c-8 0-10-10-2-14 2-8 12-10 17-6 5-4 15-2 17 6 8 4 6 14-2 14z"/><path d="M32 26h26v14H32z"/>
</svg>
<svg class="abs card-icon" style="left:895px;top:436px" viewBox="0 0 90 46" fill="none" stroke="#fff" stroke-width="2">
  <path d="M24 4h42v7H24z"/><path d="M27 11l4 32h28l4-32"/><circle cx="45" cy="25" r="8"/><path d="M41 29l8-8"/>
</svg>

<p class="abs card-text" style="left:157px;top:478px">Lorem ipsum dolor sit<br>amet, consectetur<br>adipisicing elit, sed do<br>eiusmod tempor incididunt<br>ut labore et dolore magna</p>
<p class="abs card-text" style="left:397px;top:478px">Lorem ipsum dolor sit<br>amet, consectetur<br>adipisicing elit, sed do<br>eiusmod tempor incididunt<br>ut labore et dolore magna</p>
<p class="abs card-text" style="left:637px;top:478px">Lorem ipsum dolor sit<br>amet, consectetur<br>adipisicing elit, sed do<br>eiusmod tempor incididunt<br>ut labore et dolore magna</p>
<p class="abs card-text" style="left:877px;top:478px">Lorem ipsum dolor sit<br>amet, consectetur<br>adipisicing elit, sed do<br>eiusmod tempor incididunt<br>ut labore et dolore magna</p>
<div class="btn btn-navy card-btn" style="left:180px;top:567px">Apply now</div>
<div class="btn btn-navy card-btn" style="left:396px;top:563px">Apply now</div>
<div class="btn btn-navy card-btn" style="left:648px;top:563px">Apply now</div>
<div class="btn btn-navy card-btn" style="left:878px;top:563px">Apply now</div>

<!-- sales -->
<div class="abs sales-title">Track Your Sales</div>
<p class="abs sales-copy">Lorem ipsum dolor sit amet, consectetur adipisicing elit, sed do eiusmod tempor incididunt ut labore et dolore magna aliqua. Ut enim ad minim veniam, quis nostrud exercitation ullamco laboris nisi ut aliquip ex ea commodo consequat. Duis aute irure dolor in reprehenderit in voluptate velit esse cillum dolore eu fugiat nulla pariatur. Excepteur sint occaecat cupidatat non proident, sunt in culpa qui officia deserunt mollit anim id est laborum. Sed ut perspiciatis unde omnis iste natus error sit voluptatem accusantium doloremque laudantium, totam rem aperiam, eaque ipsa quae ab illo inventore veritatis et quasi architecto beatae vitae dicta sunt explicabo. Nemo enim ipsam voluptatem quia voluptas sit aspernatur aut odit aut fugit, sed quia consequuntur magni dolores eos qui ratione voluptatem sequi nesciunt. Neque porro quisquam est, qui dolorem ipsum quia dolor sit amet, consectetur, adipisci velit, sed quia non numquam eius modi tempora incidunt ut labore et dolore magnam aliquam quaerat voluptatem.</p>

<svg class="abs chart" viewBox="534 604 509 215" font-family="Montserrat, sans-serif">
  <path d="M535 604v208a6 6 0 0 0 6 6h496a6 6 0 0 0 6-6V604" fill="#fff" stroke="#222" stroke-width="1.5"/>
  <text x="934" y="613" font-size="9.5" font-weight="700" fill="#111" text-anchor="middle">Monthly Income Stats</text>
  <text x="838" y="620" font-size="5" fill="#999">Current Year</text>
  <text x="838" y="628" font-size="5" fill="#999">Last Year</text>
  <circle cx="976" cy="617" r="3" fill="#14305a"/><circle cx="976" cy="625" r="3" fill="#1a8fd0"/>
  <g stroke="#ddd" stroke-width=".6">
    <path d="M586 649h400M586 665h400M586 680h400M586 696h400M586 711h400M586 726h400M586 742h400M586 757h400M586 772h400"/>
    <path d="M626 634v154M666 634v154M706 634v154M746 634v154M786 634v154M826 634v154M866 634v154M906 634v154M946 634v154"/>
  </g>
  <rect x="586" y="634" width="400" height="154" fill="none" stroke="#333" stroke-width="1.2"/>
  <g font-size="8.5" font-weight="700" fill="#111" text-anchor="end">
    <text x="586" y="637">11</text><text x="586" y="652">10</text><text x="586" y="668">9</text><text x="586" y="683">8</text><text x="586" y="698">7</text><text x="586" y="714">6</text><text x="586" y="729">5</text><text x="586" y="744">4</text><text x="586" y="760">3</text><text x="586" y="775">2</text><text x="586" y="790">1</text>
  </g>
  <g font-size="8.5" font-weight="700" fill="#111" text-anchor="middle">
    <text x="609" y="801">Jan</text><text x="654" y="801">Feb</text><text x="698" y="801">Apr</text><text x="743" y="801">May</text><text x="785" y="801">Jun</text><text x="826" y="801">Jul</text><text x="874" y="801">Aug</text><text x="917" y="801">Sep</text><text x="961" y="801">Oct</text><text x="1006" y="801">Nov</text>
  </g>
  <polyline points="588,750 614,737 680,722 748,708 810,726 829,694 860,678 929,637 950,630" fill="none" stroke="var(--green-light)" stroke-width="4" stroke-linejoin="round"/>
  <polyline points="590,788 608,786 677,768 730,766 800,730 846,741 860,718 888,704 946,666 986,664" fill="none" stroke="var(--green-dark)" stroke-width="4" stroke-linejoin="round"/>
  <g fill="var(--dot-pink)" stroke="#333" stroke-width=".6">
    <circle cx="614" cy="737" r="3.5"/><circle cx="748" cy="708" r="3.5"/><circle cx="810" cy="726" r="3.5"/><circle cx="829" cy="694" r="3.5"/><circle cx="929" cy="637" r="3.5"/>
  </g>
  <g fill="var(--dot-orange)" stroke="#333" stroke-width=".6">
    <circle cx="677" cy="768" r="3.5"/><circle cx="800" cy="730" r="3.5"/><circle cx="846" cy="741" r="3.5"/><circle cx="860" cy="718" r="3.5"/><circle cx="946" cy="666" r="3.5"/>
  </g>
  <rect x="794" y="668" width="66" height="13" rx="6.5" fill="#bfe0d8" stroke="#333" stroke-width=".8"/>
  <text x="824" y="678" font-size="7" fill="#fff" text-anchor="middle">$73</text>
</svg>

<!-- ingredients -->
<div class="abs band" style="top:834px;height:194px"></div>
<div class="abs band-title" style="top:840px;width:1240px">OUR Ingredients</div>

<svg class="abs card-icon" style="left:172px;top:864px;height:34px" viewBox="0 0 90 46" fill="none" stroke="#fff" stroke-width="2">
  <path d="M8 12h26l-4 32H12z"/><path d="M21 12l4-10h8"/><path d="M36 28c0-8 40-8 40 0z"/><path d="M34 32h44M36 38h40v5H36z"/>
</svg>
<svg class="abs card-icon" style="left:407px;top:864px;height:34px" viewBox="0 0 90 46" fill="none" stroke="#fff" stroke-width="2">
  <path d="M4 32c8-18 74-18 82 0-10-4-20-4-28 0-8-6-18-6-26 0-8-4-18-4-28 0z"/><path d="M32 16l4 16M58 16l-4 16M45 14v18"/>
</svg>
<svg class="abs card-icon" style="left:666px;top:864px;height:34px" viewBox="0 0 90 46" fill="none" stroke="#fff" stroke-width="2">
  <path d="M28 2h14v6l6 8v28H22V16l6-8z"/><path d="M22 26h26"/><ellipse cx="62" cy="36" rx="16" ry="8"/><circle cx="62" cy="32" r="4"/>
</svg>
<svg class="abs card-icon" style="left:900px;top:864px;height:34px" viewBox="0 0 90 46" fill="none" stroke="#fff" stroke-width="2">
  <path d="M30 18c0-12 30-12 30 0 6 0 6 8 0 8H30c-6 0-6-8 0-8z"/><path d="M32 26l13 20 13-20"/><path d="M38 26l7 10 7-10"/>
</svg>

<p class="abs card-text" style="left:157px;top:903px">Lorem ipsum dolor sit<br>amet, consectetur<br>adipisicing elit, sed do<br>eiusmod tempor incididunt<br>ut labore et dolore magna</p>
<p class="abs card-text" style="left:397px;top:903px">Lorem ipsum dolor sit<br>amet, consectetur<br>adipisicing elit, sed do<br>eiusmod tempor incididunt<br>ut labore et dolore magna</p>
<p class="abs card-text" style="left:637px;top:903px">Lorem ipsum dolor sit<br>amet, consectetur<br>adipisicing elit, sed do<br>eiusmod tempor incididunt<br>ut labore et dolore magna</p>
<p class="abs card-text" style="left:877px;top:903px">Lorem ipsum dolor sit<br>amet, consectetur<br>adipisicing elit, sed do<br>eiusmod tempor incididunt<br>ut labore et dolore magna</p>
<div class="btn btn-navy card-btn" style="left:159px;top:988px">Apply now</div>
<div class="btn btn-navy card-btn" style="left:396px;top:988px">Apply now</div>
<div class="btn btn-navy card-btn" style="left:644px;top:988px">Apply now</div>
<div class="btn btn-navy card-btn" style="left:898px;top:988px;padding-top:10px">Apply now</div>

<!-- footer -->
<div class="abs footer"></div>
<nav class="abs footer-nav">Home &nbsp;| &nbsp;About Us &nbsp;| &nbsp;Our Strategy &nbsp;| &nbsp;Board of Advisors &nbsp;| &nbsp;Striking Cares &nbsp;| &nbsp;Careers &nbsp;| &nbsp;Contact Us</nav>
<address class="abs contact">Contact Us<br>Address<br>Trayvora<br>418 Larkmoor Lane # 207<br>Brindle Falls, CA 90417<br>Need contact #<br>555 014 2290</address>
<p class="abs footer-copy">Lorem ipsum dolor sit amet, consectetur adipisicing elit, sed do eiusmod tempor incididunt ut labore et dolore magna aliqua. Ut enim ad minim veniam, quis nostrud exercitation ullamco laboris nisi ut aliquip ex ea commodo consequat. Duis aute irure dolor in reprehenderit in voluptate velit esse cillum dolo<br>re eu fugiat nulla pariatur. Excepteur sint occaecat cupidatat non proident, sunt in culpa qui officia deserunt mollit anim id est laborum. Sed ut perspiciatis unde omnis iste natus error sit voluptatem accusantium doloremque laudantium, totam rem aperiam, eaque ipsa quae ab illo inventore veritatis et quasi architecto beatae vitae dicta sunt explicabo. Nemo enim ipsam voluptatem quia voluptas sit aspernatur aut odit aut fugit, sed quia consequuntur magni dolores eos qui ratione voluptatem sequi nesciunt. Neque porro quisquam est, qui dolorem ipsum quia dolor sit amet, consectetur,</p>
<div class="abs footer-link" style="left:289px">Terms of Usage</div>
<div class="abs social" style="left:545px"></div>
<div class="abs social" style="left:594px"></div>
<div class="abs social" style="left:644px"></div>
<div class="abs connect">Connect With Us</div>
<div class="abs footer-link" style="left:782px">Privacy Policy</div>

</body>
</html>
```